Rate Card

We wish to update our rate card flyer.I have uploaded a copy of our current version, which has a black background but we want to redesign this with a cleaner and fresh look with a white background. Our new logo also needs to be used.

The stats on the why choose us need to be updated also.

- 8,000+ sales agreed
- £2.1bn sales value
- £41m savings
- 97.5% recommended
- 5,000 client testimonials

We would like a new look to this double sided flyer.

This is an urgent requirement so anyone that posts a design we like quickly will more than likely get this order!

```html
<!DOCTYPE html>
<html lang="en">
<head>
<meta charset="utf-8">
<title>Fee Menu</title>
<link href="https://fonts.googleapis.com/css2?family=Arvo:wght@400;700&display=swap" rel="stylesheet">
<style>
  :root {
    --magenta: #e6318a;
    --cyan: #00b6ea;
    --green: #9bbe3b;
    --ink: #111111;
    --grey: #6d6e70;
    --paper: #ffffff;
    --mark: #9a9a9a;
  }
  * { box-sizing: border-box; margin: 0; padding: 0; }
  html, body { width: 1200px; height: 870px; overflow: hidden; background: var(--paper); }
  .flyer {
    position: relative; width: 1200px; height: 870px; background: var(--paper);
    font-family: "Arvo", Georgia, serif; color: var(--ink);
  }
  .crop-marks { position: absolute; inset: 0; }
  .title {
    position: absolute; top: 118px; left: 0; width: 100%; text-align: center;
    font-size: 72px; font-weight: 700; color: var(--magenta); letter-spacing: -1px;
  }
  .fee-table {
    position: absolute; left: 71px; top: 233px; width: 1059px;
    border-collapse: collapse; table-layout: fixed;
  }
  .fee-table td {
    border: 2px solid var(--magenta); font-size: 29px; padding: 0 0 0 12px;
    vertical-align: middle; white-space: nowrap;
  }
  .fee-table td.value { padding-left: 28px; }
  .fee-table tr.head td { height: 78px; }
  .fee-table tr.row td { height: 76px; }
  .fee-table .head .total { font-weight: 700; padding-left: 36px; }
  .fee-table .label { background: var(--paper); }
  .row-flat .value { background: var(--magenta); }
  .row-commission .value { background: var(--cyan); }
  .row-nosale .value { background: var(--green); }
  .row-flat .total { font-weight: 700; }
  .fee-table .quote { font-size: 21px; padding-left: 22px; }
  .vat { font-size: 0.78em; }
  .footnote {
    position: absolute; top: 555px; right: 100px; font-size: 12px;
  }
  .footnote sup { font-size: 10px; }
  .advertised {
    position: absolute; left: 96px; top: 700px; font-size: 25px; color: var(--magenta);
  }
  .listing-badge { position: absolute; top: 746px; height: 40px; border-radius: 6px; }
  .badge-one { left: 91px; width: 172px; background: #b9e3da; }
  .badge-two { left: 309px; width: 142px; background: #d9c6e3; }
  .badge-three { left: 503px; width: 197px; background: #c7dcf2; }
  .brand {
    position: absolute; left: 829px; top: 734px; height: 64px;
    display: flex; align-items: center; gap: 16px;
  }
  .brand-square { width: 64px; height: 64px; background: var(--magenta); }
  .brand-name {
    font-family: "Arvo", Georgia, serif; font-size: 36px; font-weight: 400;
    color: var(--grey); line-height: 1;
  }
</style>
</head>
<body>
<main class="flyer">
  <svg class="crop-marks" width="1200" height="870" aria-hidden="true">
    <g stroke="var(--mark)" stroke-width="1">
      <line x1="40" y1="0" x2="40" y2="25"/><line x1="0" y1="40" x2="25" y2="40"/>
      <line x1="1160" y1="0" x2="1160" y2="25"/><line x1="1175" y1="40" x2="1200" y2="40"/>
      <line x1="40" y1="845" x2="40" y2="870"/><line x1="0" y1="830" x2="25" y2="830"/>
      <line x1="1160" y1="845" x2="1160" y2="870"/><line x1="1175" y1="830" x2="1200" y2="830"/>
    </g>
  </svg>

  <h1 class="title">Fee Menu</h1>

  <table class="fee-table">
    <colgroup><col style="width:248px"><col style="width:207px"><col style="width:297px"><col style="width:307px"></colgroup>
    <tr class="head">
      <td class="label"></td>
      <td class="value">Upfront</td>
      <td class="value">Completion</td>
      <td class="total">Total</td>
    </tr>
    <tr class="row row-flat">
      <td class="label">No commission</td>
      <td class="value">£495+<span class="vat">VAT</span></td>
      <td class="value">£0</td>
      <td class="value total">£495+<span class="vat">VAT</span></td>
    </tr>
    <tr class="row row-commission">
      <td class="label">Commission</td>
      <td class="value">£195+<span class="vat">VAT</span></td>
      <td class="value">£795+<span class="vat">VAT</span></td>
      <td class="value">£990+<span class="vat">VAT</span></td>
    </tr>
    <tr class="row row-nosale">
      <td class="label">No sale- No fee</td>
      <td class="value">£0</td>
      <td class="value quote">we’ll beat any quote<sup>*</sup></td>
      <td class="value quote">we’ll beat any quote<sup>*</sup></td>
    </tr>
  </table>

  <p class="footnote"><sup>*</sup>subject to a minimum fee of £1000+ <span class="vat">VAT</span></p>

  <p class="advertised">Your property advertised on</p>
  <div class="listing-badge badge-one" role="img" aria-label="Property listing site badge"></div>
  <div class="listing-badge badge-two" role="img" aria-label="Property listing site badge"></div>
  <div class="listing-badge badge-three" role="img" aria-label="Property listing site badge"></div>

  <div class="brand">
    <div class="brand-square" aria-hidden="true"></div>
    <div class="brand-name">Hearth Lane</div>
  </div>
</main>
</body>
</html>
```